Turning Lecture Halls into Studios of Bold Discovery

This is for a book cover aimed at professors in higher education who want to infuse creative thinking into their classroom. It should have the title on the cover (see name of project). Our first idea is to have a stack of academic type books on a desk in black and white and then have a colorful rainbow light thread hitting the books. However, we are open to options! It has to be sophisticated, cool, and creative ;)

Target Market(s)

Higher Education Instructors

Industry/Entity Type

education

Font styles to use
Serif
Sans Serif

Requirements
Nice to have
• a creative feel of some sort
Should not have
• lightbulbs

```html
<!DOCTYPE html>
<html lang="en">
<head>
<meta charset="utf-8">
<title>Turning Lecture Halls into Studios of Bold Discovery – Book Cover</title>
<link rel="stylesheet" href="https://fonts.googleapis.com/css2?family=EB+Garamond:wght@400;500;600;700&family=Sacramento&display=swap">
<style>
  :root {
    --page-bg: #dedede;
    --paper: #ffffff;
    --ink: #111111;
    --orange-light: #ff8a00;
    --orange-deep: #ee4200;
    --rule: #f39a1e;
    --art-warm: #f6d2b8;
    --art-cool: #eeeeee;
  }
  * { box-sizing: border-box; margin: 0; padding: 0; }
  html, body {
    width: 1200px; height: 1200px; overflow: hidden;
    background: var(--page-bg);
  }
  .cover {
    position: absolute; left: 30px; top: 189px;
    width: 1140px; height: 822px;
    background: var(--paper);
    display: flex;
    font-family: "EB Garamond", Georgia, serif;
    color: var(--ink);
  }
  .accent {
    background: linear-gradient(180deg, var(--orange-light), var(--orange-deep));
    -webkit-background-clip: text; background-clip: text;
    color: transparent;
  }
  .script, .t-script {
    font-family: "Sacramento", cursive; font-weight: 400; text-transform: none;
  }

  /* ---------- back cover ---------- */
  .back { position: relative; width: 526px; height: 100%; }
  .back-title {
    position: absolute; top: 38px; left: 0; right: 0;
    text-align: center; text-transform: uppercase; line-height: 1;
  }
  .back-title .t-big { font-size: 40px; font-weight: 700; display: block; }
  .back-title .t-small { font-size: 24px; font-weight: 500; display: block; margin-top: 4px; }
  .back-title .t-script {
    display: flex; align-items: center; justify-content: center; gap: 10px;
    font-size: 28px; margin: 4px 0 2px;
  }
  .back-title .t-script::before, .back-title .t-script::after {
    content: ""; width: 48px; height: 1px; background: var(--rule);
  }
  .blurb {
    position: absolute; left: 42px; right: 42px;
    font-size: 12px; line-height: 16px; text-align: justify; text-align-last: center;
  }
  .blurb p + p { margin-top: 12px; }
  .blurb-main { top: 243px; }
  .author-mark {
    position: absolute; top: 397px; left: 50%; transform: translateX(-50%);
    width: 127px; height: 127px; border-radius: 50%;
    background: linear-gradient(180deg, var(--orange-light), var(--orange-deep));
  }
  .back-author {
    position: absolute; top: 539px; left: 0; right: 0; text-align: center;
    font-size: 23px; line-height: 28px; letter-spacing: 0.2em; font-weight: 500;
  }
  .blurb-bio { top: 581px; }

  /* ---------- spine ---------- */
  .spine { position: relative; width: 74px; height: 100%; }
  .spine-title, .spine-author {
    position: absolute; left: 50%; white-space: nowrap;
    transform-origin: 0 0; transform: rotate(90deg);
    text-transform: uppercase;
  }
  .spine-title { top: 46px; margin-left: 28px; font-size: 22px; line-height: 1; font-weight: 500; }
  .spine-title .line { display: block; }
  .spine-title .line + .line { margin-top: 2px; }
  .spine-title .script { font-size: 18px; }
  .spine-author { top: 536px; margin-left: 12px; font-size: 23px; letter-spacing: 0.2em; font-weight: 500; }

  /* ---------- front cover ---------- */
  .front { position: relative; width: 540px; height: 100%; }
  .front-art {
    position: absolute; left: 25px; top: 46px; width: 470px; height: 284px;
  }
  .front-title {
    position: absolute; top: 372px; left: 0; right: 0;
    text-align: center; text-transform: uppercase; line-height: 1;
  }
  .front-title .t-big { display: block; font-size: 82px; font-weight: 700; line-height: 0.95; }
  .front-title .t-small { display: block; font-size: 44px; font-weight: 500; margin-top: 6px; }
  .front-title .t-script {
    display: flex; align-items: center; justify-content: center; gap: 14px;
    font-size: 52px; margin: 6px 0 8px; padding: 0 24px;
  }
  .front-title .t-script::before, .front-title .t-script::after {
    content: ""; flex: 1; height: 2px; background: var(--rule);
  }
  .front-author {
    position: absolute; top: 752px; left: 0; right: 0; text-align: center;
    font-size: 28px; letter-spacing: 0.2em; font-weight: 500;
  }
</style>
</head>
<body>
  <main class="cover">
    <section class="back">
      <h2 class="back-title">
        <span class="t-big accent">Turning</span>
        <span class="t-small">Lecture Halls</span>
        <span class="t-script">into studios of</span>
        <span class="t-big accent">Bold</span>
        <span class="t-small">Discovery</span>
      </h2>
      <div class="blurb blurb-main">
        <p>Creativity is not a talent reserved for artists; it is a habit every lecturer can cultivate, in any discipline and at any level.</p>
        <p>Drawing on classroom research and years of teaching across disciplines, this practical guide shows how to redesign assignments, discussions and assessments so that students take intellectual risks, test ideas openly and build work they are proud of. Each chapter closes with ready-to-use activities, reflection prompts and examples you can try in your very next class.</p>
      </div>
      <div class="author-mark" role="img" aria-label="Author portrait placeholder"></div>
      <p class="back-author">AUTHOR’S NAME</p>
      <div class="blurb blurb-bio">
        <p>The author has taught in universities for two decades, leading workshops on creative pedagogy and course design for faculty who want their lecture halls to feel more like studios of bold discovery, and writes often on teaching, curiosity and risk.</p>
      </div>
    </section>

    <section class="spine">
      <p class="spine-title">
        <span class="line"><span class="accent">Turning</span> Lecture Halls</span>
        <span class="line"><span class="script">into studios of</span> <span class="accent">Bold</span> Discovery</span>
      </p>
      <p class="spine-author">AUTHOR’S NAME</p>
    </section>

    <section class="front">
      <svg class="front-art" viewBox="0 0 470 284" role="img" aria-label="Sketched illustration of a student reading between two tall stacks of books on a grassy hill under clouds">
        <defs>
          <radialGradient id="artGlow" cx="50%" cy="70%" r="55%">
            <stop offset="0%" stop-color="var(--art-warm)"/>
            <stop offset="100%" stop-color="var(--art-cool)"/>
          </radialGradient>
        </defs>
        <rect width="470" height="284" rx="6" fill="url(#artGlow)"/>
      </svg>
      <h1 class="front-title">
        <span class="t-big accent">Turning</span>
        <span class="t-small">Lecture Halls</span>
        <span class="t-script">into studios of</span>
        <span class="t-big accent">Bold</span>
        <span class="t-small">Discovery</span>
      </h1>
      <p class="front-author">AUTHOR’S NAME</p>
    </section>
  </main>
</body>
</html>
```